Business Card Design

We need a business card designed for a new company based in Melbourne called KPo solutions. KPo solutions provides management consulting specialising in the health and social services sector.

KPo solutions offer a unique set of specialist skills │dealing with all levels of government │ unique communication skills│intimate knowledge of the health sector │solutions tailored to unique circumstances.

KPo solutions takes on a select number of clients at any one time, this ensures that your organisation receives the attention required. On larger projects, KPo solutions join up with other consultants to bring specialist skills to a project.
Updates

This is the first time I have used Pattern Hive and thank you all for responding. The variation is amazing and makes it hard to decide. I have to ask some of my friends to give me their views. The response is fantastic. The one I pick will basically be the most visually appealing

Industry/Entity Type

Management Consulting

Contact Information for Business Card

Martin Hollis, Principal, KPo solutions, 14 Calloway Ave, Westbridge VIC 3094, 0438 712 304, martinh@kposolutions.com.au, www.kposolutions.com.au

```html
<!DOCTYPE html>
<html lang="en">
<head>
<meta charset="utf-8">
<title>KPo solutions – Business Card</title>
<link href="https://fonts.googleapis.com/css2?family=Questrial&display=swap" rel="stylesheet">
<style>
  :root {
    --red-bright: #f2051f;
    --red-mid: #d6000f;
    --red-deep: #b3000a;
    --red-dark: #9c0008;
    --ink-light: #ffffff;
    --ink-dark: #2a1212;
    --page: #ffffff;
  }
  html, body {
    margin: 0;
    padding: 0;
    width: 1200px;
    height: 741px;
    overflow: hidden;
    background: var(--page);
    font-family: "Questrial", "Century Gothic", sans-serif;
  }
  .card {
    position: relative;
    width: 1200px;
    height: 679px;
    overflow: hidden;
    background: var(--red-mid);
  }
  .card-waves {
    position: absolute;
    inset: 0;
    width: 100%;
    height: 100%;
  }
  .brand-name {
    position: absolute;
    left: 0;
    right: 0;
    top: 140px;
    text-align: center;
    color: var(--ink-light);
    font-size: 104px;
    line-height: 1;
    letter-spacing: 2px;
    margin: 0;
    font-weight: 400;
  }
  .person {
    position: absolute;
    left: 91px;
    top: 458px;
    margin: 0;
  }
  .person-name {
    display: block;
    color: var(--ink-light);
    font-size: 52px;
    line-height: 56px;
  }
  .person-role {
    display: block;
    color: var(--ink-dark);
    font-size: 32px;
    line-height: 30px;
  }
  .contact {
    position: absolute;
    right: 80px;
    top: 526px;
    margin: 0;
    padding: 0;
    list-style: none;
    text-align: right;
  }
  .contact-item {
    display: flex;
    justify-content: flex-end;
    align-items: center;
    gap: 10px;
    font-size: 34px;
    line-height: 35px;
    color: var(--ink-light);
  }
  .contact-item--web { color: var(--ink-dark); }
  .contact-icon {
    width: 24px;
    height: 24px;
    flex: none;
    fill: var(--ink-dark);
  }
</style>
</head>
<body>
  <div class="card">
    <svg class="card-waves" viewBox="0 0 1200 679" preserveAspectRatio="none" aria-hidden="true">
      <defs>
        <linearGradient id="wave-top" x1="0" y1="0" x2="1" y2="1">
          <stop offset="0" stop-color="var(--red-bright)"/>
          <stop offset="1" stop-color="var(--red-deep)"/>
        </linearGradient>
        <linearGradient id="wave-low" x1="0" y1="0" x2="1" y2="0">
          <stop offset="0" stop-color="var(--red-mid)"/>
          <stop offset="1" stop-color="var(--red-dark)"/>
        </linearGradient>
      </defs>
      <rect width="1200" height="679" fill="url(#wave-low)"/>
      <path d="M0 0 H1200 V679 C1050 520 760 400 0 290 Z" fill="url(#wave-top)"/>
      <path d="M0 70 C300 10 800 10 1200 110 V0 H0 Z" fill="var(--red-dark)" opacity="0.55"/>
      <path d="M0 80 C350 25 820 30 1200 125 V140 C820 50 350 45 0 95 Z" fill="var(--red-bright)" opacity="0.6"/>
      <path d="M1030 60 C1120 140 1180 220 1200 260 V0 H1100 Z" fill="var(--red-bright)" opacity="0.35"/>
      <path d="M0 290 C700 380 1050 500 1200 679 H0 Z" fill="var(--red-deep)" opacity="0.45"/>
    </svg>

    <h1 class="brand-name">KPo solutions</h1>

    <p class="person">
      <span class="person-name">Martin Hollis</span>
      <span class="person-role">Principal</span>
    </p>

    <ul class="contact">
      <li class="contact-item contact-item--phone">
        0438 712 304
        <svg class="contact-icon" viewBox="0 0 24 24" aria-hidden="true"><path d="M3 9c0-3 4-5 9-5s9 2 9 5v2h-5V9H8v2H3z"/><rect x="5" y="12" width="14" height="8" rx="1.5"/></svg>
      </li>
      <li class="contact-item contact-item--address">
        Calloway Ave, Westbridge VIC 3094
        <svg class="contact-icon" viewBox="0 0 24 24" aria-hidden="true"><rect x="11" y="2" width="2.5" height="20"/><path d="M4 5h15l3 2.5-3 2.5H4z"/><path d="M20 12H5l-3 2.5L5 17h15z"/></svg>
      </li>
      <li class="contact-item contact-item--email">
        martinh@kposolutions.com.au
        <svg class="contact-icon" viewBox="0 0 24 24" aria-hidden="true"><path d="M2 6h20v1l-10 7L2 7z"/><path d="M2 9l10 7 10-7v10H2z"/></svg>
      </li>
      <li class="contact-item contact-item--web">
        www.kposolutions.com.au
        <svg class="contact-icon" viewBox="0 0 24 24" aria-hidden="true"><circle cx="12" cy="12" r="10"/><path d="M8 6c2 1 3 3 1 5s0 4 2 5M15 5c-1 2 1 3 3 3M14 20c0-2 2-3 4-3" stroke="#c8000f" stroke-width="1.6" fill="none"/></svg>
      </li>
    </ul>
  </div>
</body>
</html>
```